Process Diagram - Circular Economy

I would like for a designer to take this rough sketch and turn it into a high quality design which can be used in a business presentation. Seeking to get both PDF and Jpeg file versions of the finished product.

Colours don't have to be the exact same as the rough sketch PDF, the green used is pretty ugly so open to some changes.

Target Market(s)

Corporate audience

Requirements
Must have
• Clear text for each party; VENOR, KORMIT, BUYER

Smaller text for the functions; marketing, recovery, logistics, cleaning, decontamination, testing & re-certification, storage, engineering suitability

```html
<!DOCTYPE html>
<html lang="en">
<head>
<meta charset="utf-8">
<title>Circular Economy Process – Vendor, Kormit, Buyer</title>
<link href="https://fonts.googleapis.com/css2?family=Oswald:wght@500;600&family=Barlow+Semi+Condensed:wght@500&display=swap" rel="stylesheet">
<style>
  :root {
    --ink: #3f3f41;
    --white: #ffffff;
    --vendor-blue: #0033aa;
    --vendor-deep: #0022a0;
    --sky: #00b9e8;
    --leaf: #63bc00;
    --leaf-soft: #5fbb1e;
  }
  html, body {
    margin: 0;
    padding: 0;
    width: 1200px;
    height: 849px;
    overflow: hidden;
    background: var(--white);
  }
  .diagram {
    display: block;
    width: 1200px;
    height: 849px;
  }
  .stage-title {
    font-family: "Oswald", sans-serif;
    font-weight: 600;
    fill: var(--ink);
  }
  .party-name {
    font-family: "Oswald", sans-serif;
    font-weight: 600;
    fill: var(--white);
  }
  .function-label {
    font-family: "Barlow Semi Condensed", sans-serif;
    font-weight: 500;
    font-size: 38px;
    fill: var(--white);
  }
  .stop-leaf { stop-color: var(--leaf-soft); }
  .stop-sky { stop-color: var(--sky); }
  .stop-blue { stop-color: var(--vendor-blue); }
  .stop-deep { stop-color: var(--vendor-deep); }
  .buyer-arrow { fill: var(--leaf); }
</style>
</head>
<body>
<svg class="diagram" viewBox="0 0 2339 1654" xmlns="http://www.w3.org/2000/svg" role="img" aria-label="Circular economy process: from vendor at end of life, through Kormit services, to buyer for a new life">
  <defs>
    <linearGradient id="loop-left" gradientUnits="userSpaceOnUse" x1="820" y1="860" x2="1060" y2="1260">
      <stop offset="0" class="stop-leaf"/>
      <stop offset="0.35" class="stop-leaf"/>
      <stop offset="1" class="stop-sky"/>
    </linearGradient>
    <linearGradient id="loop-right" gradientUnits="userSpaceOnUse" x1="0" y1="820" x2="0" y2="1160">
      <stop offset="0" class="stop-deep"/>
      <stop offset="1" class="stop-sky"/>
    </linearGradient>
    <linearGradient id="vendor-band" gradientUnits="userSpaceOnUse" x1="335" y1="0" x2="1400" y2="0">
      <stop offset="0" class="stop-deep"/>
      <stop offset="0.5" class="stop-blue"/>
      <stop offset="1" class="stop-deep"/>
    </linearGradient>
    <linearGradient id="marketing-band" gradientUnits="userSpaceOnUse" x1="1030" y1="0" x2="1220" y2="0">
      <stop offset="0" class="stop-sky"/>
      <stop offset="1" class="stop-blue"/>
    </linearGradient>
  </defs>

  <!-- Stage titles -->
  <text class="stage-title" x="335" y="458" font-size="90" textLength="310" lengthAdjust="spacingAndGlyphs">End of Life</text>
  <text class="stage-title" x="1487" y="458" font-size="90" textLength="258" lengthAdjust="spacingAndGlyphs">New Life</text>

  <!-- Buyer arrow -->
  <polygon class="buyer-arrow" points="1120,650 1752,538 1752,502 1962,583 1769,771 1766,720 1352,792"/>

  <!-- Kormit loop -->
  <g class="service-loop">
    <path fill="url(#loop-left)" d="M1083,648 A322,322 0 0 0 1083,1292 L1083,1111 A141,141 0 0 1 1083,829 Z"/>
    <path fill="url(#loop-right)" d="M1083,648 A322,322 0 0 1 1083,1292 L1083,1111 A141,141 0 0 0 1083,829 Z"/>
  </g>

  <!-- Vendor band -->
  <path fill="url(#vendor-band)" d="M335,512 L1120,650 C1220,665 1330,730 1397,900 L1223,975 C1190,880 1150,845 1105,830 L335,696 Z"/>

  <!-- Marketing band -->
  <path fill="url(#marketing-band)" d="M498,725 L1105,830 C1170,845 1215,890 1223,975 C1190,920 1150,900 1090,892 L498,788 Z"/>

  <!-- Party names -->
  <text class="party-name" x="400" y="650" font-size="108" textLength="210" lengthAdjust="spacingAndGlyphs" transform="rotate(10 400 650)">VENDOR</text>
  <text class="party-name" x="1550" y="693" font-size="108" textLength="170" lengthAdjust="spacingAndGlyphs" transform="rotate(-10 1550 693)">BUYER</text>
  <text class="party-name" x="1130" y="1168" font-size="90" textLength="190" lengthAdjust="spacingAndGlyphs">KORMIT</text>

  <!-- Function labels -->
  <text class="function-label" x="530" y="780" transform="rotate(9.5 530 780)">Marketing</text>
  <text class="function-label" x="1005" y="755">Recovery</text>
  <text class="function-label" x="1220" y="880">Logistics</text>
  <text class="function-label" x="1224" y="1047">Cleaning</text>
  <text class="function-label" x="998" y="1240">Decontamination</text>
  <text class="function-label" x="842" y="1130">Testing &amp;</text>
  <text class="function-label" x="842" y="1170">Re-certification</text>
  <text class="function-label" x="795" y="1047">Storage</text>
  <text class="function-label" x="780" y="912">Engineering</text>
  <text class="function-label" x="780" y="952">Suitability</text>
</svg>
</body>
</html>
```